TEK Logistics - Banner 2.5' x 8' for 20+ locations

Need a banner designed that will pop. This banner will be displayed at over 20 of our transportation facilities. Goal is for the banner to grab the attention of employees, contractors and clients and help reinforce our mission and core values. Designed needs to include TEK Logo, our core values and mission statement. Red and Black are the main company colors and we need to stay within that theme and color pallet. Attached is a previous version that was too basic and boring. Willing to consider a design that excludes the mission statement.

Gathering more feedback

```html
<!DOCTYPE html>
<html lang="en">
<head>
<meta charset="utf-8">
<title>TEK Logistics – Core Values Banner</title>
<link href="https://fonts.googleapis.com/css2?family=Montserrat:wght@700;800&family=Hind:wght@500;600&display=swap" rel="stylesheet">
<style>
  :root {
    --backdrop: #2b2a27;
    --banner: #ffffff;
    --brand-red: #d52b1e;
    --brand-black: #1d1d1b;
    --text: #2a2a2a;
  }
  * { box-sizing: border-box; margin: 0; padding: 0; }
  html, body {
    width: 1200px; height: 1200px; overflow: hidden;
    background: var(--backdrop);
  }
  .banner {
    position: absolute; left: 40px; top: 425px;
    width: 1120px; height: 350px;
    background: var(--banner);
    overflow: hidden;
    font-family: "Hind", Arial, sans-serif;
    color: var(--text);
  }
  .section-tab {
    position: absolute; left: 0; height: 37px;
    background: var(--brand-red);
    clip-path: polygon(0 0, 100% 0, calc(100% - 10px) 100%, 0 100%);
    color: #fff;
    font-family: "Montserrat", Arial, sans-serif;
    font-weight: 700; font-size: 23px;
    line-height: 39px; padding-left: 34px;
    letter-spacing: 0.2px;
  }
  .section-slash {
    position: absolute; width: 17px; height: 37px;
    background: var(--brand-black);
    clip-path: polygon(0 0, 6px 0, 100% 100%, 11px 100%);
  }
  .tab-values { top: 34px; width: 289px; }
  .slash-values { top: 34px; left: 292px; }
  .tab-mission { top: 217px; width: 386px; }
  .slash-mission { top: 217px; left: 381px; }

  .values-list {
    position: absolute; top: 88px; list-style: none;
  }
  .values-list.col-left { left: 35px; }
  .values-list.col-right { left: 492px; }
  .values-list li {
    display: flex; align-items: center; gap: 10px;
    height: 35px; font-size: 22px; font-weight: 500;
  }
  .tick { width: 16px; height: 16px; flex: none; }

  .mission-text {
    position: absolute; left: 35px; top: 264px; width: 1060px;
    font-size: 21.5px; font-weight: 500; line-height: 28px;
  }

  .brand-name {
    position: absolute; left: 880px; top: 80px;
    display: flex; align-items: center; gap: 12px;
    font-family: "Hind", Arial, sans-serif;
    font-weight: 600; font-size: 34px;
    color: var(--brand-red);
  }
  .brand-dot {
    width: 22px; height: 22px; border-radius: 50%;
    background: var(--brand-red);
  }
</style>
</head>
<body>
  <main class="banner">
    <div class="section-tab tab-values">OUR CORE VALUES:</div>
    <div class="section-slash slash-values"></div>

    <ul class="values-list col-left">
      <li><svg class="tick" viewBox="0 0 16 16"><circle cx="8" cy="8" r="8" fill="#d52b1e"/><path d="M4.5 8.3l2.3 2.2 4.6-4.7" fill="none" stroke="#fff" stroke-width="2"/></svg>Do the right things for the right reasons</li>
      <li><svg class="tick" viewBox="0 0 16 16"><circle cx="8" cy="8" r="8" fill="#d52b1e"/><path d="M4.5 8.3l2.3 2.2 4.6-4.7" fill="none" stroke="#fff" stroke-width="2"/></svg>Pursue growth and development</li>
      <li><svg class="tick" viewBox="0 0 16 16"><circle cx="8" cy="8" r="8" fill="#d52b1e"/><path d="M4.5 8.3l2.3 2.2 4.6-4.7" fill="none" stroke="#fff" stroke-width="2"/></svg>Build a positive team atmosphere</li>
    </ul>
    <ul class="values-list col-right">
      <li><svg class="tick" viewBox="0 0 16 16"><circle cx="8" cy="8" r="8" fill="#d52b1e"/><path d="M4.5 8.3l2.3 2.2 4.6-4.7" fill="none" stroke="#fff" stroke-width="2"/></svg>Deliver WOW through service</li>
      <li><svg class="tick" viewBox="0 0 16 16"><circle cx="8" cy="8" r="8" fill="#d52b1e"/><path d="M4.5 8.3l2.3 2.2 4.6-4.7" fill="none" stroke="#fff" stroke-width="2"/></svg>Do everything Safely</li>
      <li><svg class="tick" viewBox="0 0 16 16"><circle cx="8" cy="8" r="8" fill="#d52b1e"/><path d="M4.5 8.3l2.3 2.2 4.6-4.7" fill="none" stroke="#fff" stroke-width="2"/></svg>Have Fun</li>
    </ul>

    <div class="brand-name"><span class="brand-dot"></span>TEK Logistics</div>

    <div class="section-tab tab-mission">OUR MISSION STATEMENT:</div>
    <div class="section-slash slash-mission"></div>
    <p class="mission-text">Provide the best customer experience while creating an environment of growth and opportunity for our customers, employees, and service providers.</p>
  </main>
</body>
</html>
```